Briefpapier und Visitenkarten
Zielgruppe
Das Design soll Herren im mittleren bis hohen Alter ansprechen.
Aufgabenstellung
Benötigt wird ein Briefpapier für die Koresspondenz und die Rechnungen. Ein Logo ist vorhanden und muss ins Briefpapier und auf die Visitenkarten einbebunden werden.

```html
<!DOCTYPE html>
<html lang="de">
<head>
<meta charset="utf-8">
<title>Normbrief nach DIN 676 – nordwerk makler</title>
<link href="https://fonts.googleapis.com/css2?family=Arimo:wght@400;700&display=swap" rel="stylesheet">
<style>
  :root {
    --brand-red: #c8102e;
    --ink: #111111;
    --mark-grey: #b5b5b5;
    --paper: #ffffff;
  }
  * { margin: 0; padding: 0; box-sizing: border-box; }
  html, body { width: 848px; height: 1200px; overflow: hidden; background: var(--paper); }
  .letter {
    position: relative;
    width: 848px; height: 1200px;
    overflow: hidden;
    background: var(--paper);
    font-family: "Arimo", Arial, sans-serif;
    color: var(--ink);
  }
  .brand {
    position: absolute; top: 68px; left: 0; width: 848px;
    display: flex; justify-content: center; align-items: center; gap: 12px;
  }
  .brand-square { width: 18px; height: 18px; background: var(--brand-red); }
  .brand-name { font-size: 40px; font-weight: 400; color: var(--brand-red); letter-spacing: 0.5px; }

  .sender-line {
    position: absolute; top: 181px; left: 135px;
    font-size: 7px; font-weight: 700;
  }
  .recipient {
    position: absolute; top: 199px; left: 97px;
    font-size: 17px; line-height: 20.1px; font-style: normal;
  }
  .info-block {
    position: absolute; top: 203px; left: 507px;
    font-size: 12.8px; line-height: 14.6px;
  }
  .info-block .gap { height: 14.6px; }

  .subject {
    position: absolute; top: 392px; left: 97px;
    font-size: 16.5px; font-weight: 700;
  }
  .body {
    position: absolute; top: 443px; left: 97px; width: 742px;
    font-size: 17.6px; line-height: 21.4px;
  }
  .body p { margin-bottom: 19px; }
  .body .signer { margin-top: 40px; }

  .fold-mark {
    position: absolute; left: 14px; width: 26px; height: 1px; background: var(--mark-grey);
  }
  .fold-mark.upper { top: 423px; }
  .fold-mark.middle { top: 600px; }
  .fold-mark.lower { top: 849px; }

  .footer {
    position: absolute; top: 1089px; left: 97px; width: 740px;
    font-size: 7.2px; line-height: 9.4px;
  }
  .footer .col { position: absolute; top: 0; }
  .footer .col strong { font-weight: 700; }
  .footer .col-house { left: 0; }
  .footer .col-post { left: 205px; }
  .footer .col-contact { left: 410px; }
  .footer .col-bank { left: 614px; }
</style>
</head>
<body>
<div class="letter">

  <header class="brand">
    <span class="brand-square"></span>
    <span class="brand-name">nordwerk makler</span>
  </header>

  <div class="sender-line">Feldberg Handels GmbH · Lindenallee 11 · 10000 Sonnfeld</div>

  <address class="recipient">
    Nicht nachsenden<br>
    Persönlich<br>
    Einschreiben<br>
    Klarwerk GmbH<br>
    Herr / Frau Interessent<br>
    Ahornweg 7<br>
    54321 Talheim<br>
    Deutschland
  </address>

  <div class="info-block">
    Ihr Zeichen:<br>
    Ihre Nachricht vom:
    <div class="gap"></div>
    Unser Zeichen:<br>
    Unsere Nachricht vom:
    <div class="gap"></div><div class="gap"></div>
    Name: Jonas Brettschneider<br>
    Telefon: +49-555-1472<br>
    E-Mail: j.brettschneider@feldberg-handel.de<br>
    Internet: www.feldberg-handel.de
  </div>

  <div class="fold-mark upper"></div>
  <div class="fold-mark middle"></div>
  <div class="fold-mark lower"></div>

  <h1 class="subject">Normbrief nach DIN 676</h1>

  <main class="body">
    <p>Sehr geehrter Herr / Frau Interessent,</p>
    <p>dieser Brief ist nach DIN 676, Vorduck B (erweiterter Briefkopf) mit Informationsblock erstellt.</p>
    <p>Der Vordruck ist in mehreren Ebenen aufgebaut. Für diejenigen, die es genau wissen wollen, sind die Ebenen „Layout“ und „Beschriftung Layout“ eingebaut. Die kann man auch löschen. In der Ebene „Beispiel - fester Text“ sind die feststehenden Elemente des Briefes enthalten. Sie sollte nach der Erarbeitung gesperrt werden. Es macht natürlich auch Sinn diesen Teil als Mustervorlage anzulegen (Mustervorlage A für die 1. Seite des Briefes und Mustervorlage B für die Folgeseiten). Die Ebene „Text“ enthält den variablen Teil des Briefes. Es macht natür­lich auch Sinn diesen Teil als Mustervorlage anzulegen (Mustervorlage A für die 1. Seite des Briefes und Mustervorlage B für die Folgeseiten). Die Ebene „Text“ enthält den variablen Teil des Briefes. Für die Absatzformate ist ein Vorschlag enthalten.</p>
    <p>Für die Absatzformate ist ein Vorschlag enthalten.</p>
    <p>Mit freundlichen Güßen</p>
    <p>Feldberg Handels GmbH</p>
    <p class="signer">Name des Unterzeichners</p>
    <p>Anlagen</p>
    <p>Verteiler</p>
  </main>

  <footer class="footer">
    <div class="col col-house">Hausanschrift<br><strong>Feldberg Handels GmbH<br>Lindenallee 11<br>10000 Sonnfeld</strong></div>
    <div class="col col-post">Postanschrift<br><strong>Feldberg Handels GmbH<br>PF 248<br>10001 Sonnfeld</strong></div>
    <div class="col col-contact">Telefon: +49-555-1400<br>Telefax: +49-555-1499<br>www.feldberg-handel.de<br>E-Mail: post@feldberg-handel.de</div>
    <div class="col col-bank">Ust-ID: DE 482 117<br>St-Nr.:<br>HRA:<br>Konto-Nr.:<br>Bankleitzahl:</div>
  </footer>

</div>
</body>
</html>
```